Northwind Harbor Capital Business Card

Creativity is a must. We'd prefer something different from the run of the mill.

The emphasis in our name is on Harbor. We'd like to see some vertical designs.

I've added a copy of our logo and the QR code we'd like to use. Our tag line is A QUIET HAND ON EVERY VENTURE™

Business Card Data
Name: Ron Vickers
Address: 24519 Palmetto Ridge Rd, Odessa, FL 33556
Main: 813-555-0142
Cell: 813-555-0187
Fax: 813-555-0163
Email: rvickers@northwindharbor.example
URL: www.northwindharbor.example

We use Printlyx.com for our business cards and will need a fully editable psd file using their template.

Target Market(s)

We need a new business card design for a US based private equity firm. Our clients are investors and business owners.

Industry/Entity Type

Business

Font styles to use
Sans Serif

Requirements
Must have
• QR code
Creativity
You're welcome to change the logo color palette

```html
<!DOCTYPE html>
<html lang="en">
<head>
<meta charset="utf-8">
<title>Northwind Harbor Capital – Business Card</title>
<link rel="stylesheet" href="https://fonts.googleapis.com/css2?family=Open+Sans:wght@400;600;700&display=swap">
<style>
  :root {
    --backdrop: #ebe8e3;
    --card-light: #fbfbfa;
    --card-dark: #17223a;
    --ink-navy: #1c2a44;
    --ink-grey: #3c3f45;
    --brand-green: #2e9a2f;
    --brand-blue: #2a86c8;
    --paper-white: #ffffff;
    --qr-frame: #d9dde4;
  }
  * { margin: 0; padding: 0; box-sizing: border-box; }
  html, body { width: 1200px; height: 961px; overflow: hidden; }
  body {
    background: var(--backdrop);
    font-family: "Open Sans", Arial, sans-serif;
  }
  .canvas { position: relative; width: 1200px; height: 961px; }

  .card {
    position: absolute;
    border-radius: 3px;
    box-shadow: 0 10px 24px rgba(0,0,0,0.12);
  }

  /* Wordmark: one colour, one weight; Harbor emphasised by scale */
  .wordmark {
    font-weight: 600;
    text-transform: uppercase;
    line-height: 1.1;
  }
  .wordmark .wm-top { display: block; font-size: 17px; letter-spacing: 4px; }
  .wordmark .wm-main { display: block; font-size: 36px; letter-spacing: 1.5px; }
  .wordmark .wm-sub { display: block; font-size: 14px; letter-spacing: 7px; margin-top: 2px; }

  .brand-dot {
    position: absolute;
    border-radius: 50%;
    background: var(--brand-green);
  }

  /* Front card – horizontal */
  .card--front { left: 90px; top: 110px; width: 560px; height: 320px; background: var(--card-light); }
  .card--front .wordmark { position: absolute; left: 44px; top: 46px; color: var(--ink-navy); }
  .card--front .brand-dot { right: 50px; top: 40px; width: 96px; height: 96px; }
  .contact {
    position: absolute; right: 44px; bottom: 30px;
    text-align: right; color: var(--ink-grey);
  }
  .contact .person {
    font-size: 20px; font-weight: 700; color: var(--ink-navy);
    letter-spacing: 0.5px; margin-bottom: 12px;
  }
  .contact .line { font-size: 12.5px; line-height: 1.6; white-space: nowrap; }
  .contact .label { font-weight: 700; }
  .label--blue { color: var(--brand-blue); }
  .label--green { color: var(--brand-green); }

  /* Back card – vertical */
  .card--back {
    left: 740px; top: 410px; width: 320px; height: 520px;
    background: var(--card-dark);
    text-align: center;
  }
  .card--back .brand-dot { left: 118px; top: 44px; width: 84px; height: 84px; }
  .card--back .wordmark {
    position: absolute; left: 0; right: 0; top: 152px;
    color: var(--paper-white);
  }
  .tagline {
    position: absolute; left: 0; right: 0; top: 276px;
    font-size: 15px; font-weight: 400; line-height: 1.35; text-transform: uppercase;
  }
  .tagline .first { color: var(--paper-white); display: block; }
  .tagline .second { color: var(--brand-blue); display: block; }
  .qr-slot {
    position: absolute; left: 105px; bottom: 44px;
    width: 110px; height: 110px;
    background: var(--paper-white);
    border: 6px solid var(--qr-frame);
    border-radius: 4px;
  }
</style>
</head>
<body>
<main class="canvas">
  <section class="card card--front" aria-label="Business card front">
    <p class="wordmark">
      <span class="wm-top">Northwind</span>
      <span class="wm-main">Harbor</span>
      <span class="wm-sub">Capital</span>
    </p>
    <div class="brand-dot" aria-hidden="true"></div>
    <div class="contact">
      <p class="person">RON VICKERS</p>
      <p class="line">24519 Palmetto Ridge Rd, Odessa, FL 33556</p>
      <p class="line"><span class="label label--blue">Main:</span> 813-555-0142 · <span class="label label--blue">Cell:</span> 813-555-0187 · <span class="label label--blue">Fax:</span> 813-555-0163</p>
      <p class="line"><span class="label label--green">Email:</span> rvickers@northwindharbor.example · <span class="label label--green">Web:</span> www.northwindharbor.example</p>
    </div>
  </section>

  <section class="card card--back" aria-label="Business card back, vertical">
    <div class="brand-dot" aria-hidden="true"></div>
    <p class="wordmark">
      <span class="wm-top">Northwind</span>
      <span class="wm-main">Harbor</span>
      <span class="wm-sub">Capital</span>
    </p>
    <p class="tagline">
      <span class="first">A quiet hand on</span>
      <span class="second">every venture™</span>
    </p>
    <div class="qr-slot" role="img" aria-label="QR code linking to the company website"></div>
  </section>
</main>
</body>
</html>
```